Business Card Makeover. Recreate a sleek modern design for our business card.

DO NOT COPY OUR CURRENT DESIGN. MUST BE ONE SIDED BUSINESS CARD.
Create a new business card design, using our new logo. Attached is a sample of our current design and new logo. Please note the address and email will change. The new address is 417 Marlowe West Palm Beach 33401 and our website will be www.veltradunmore.com.

We are an architectural and interior design firm. We prefer a clean modern look. Something that is refined and emulates excellence.

Industry/Entity Type

Architecture

Contact Information for Business Card

clean modern look, please do not copy our attached design.

Font styles to use
Other font styles liked:
• see attached business card font

Colors

Designer to choose colors to be used in the design.

Requirements
Must have
• Must have a modern appeal and resemble our current branding.
Nice to have
• modern font, our logo, legible name and titles progressive design
Should not have
• Do not add colors not reflected in our branding. Should not look like our current card.

```html
<!DOCTYPE html>
<html lang="en">
<head>
<meta charset="utf-8">
<title>Veltra Dunmore — Business Card</title>
<link href="https://fonts.googleapis.com/css2?family=Lato:wght@400;700;900&display=swap" rel="stylesheet">
<style>
  :root {
    --backdrop: #1c1c1c;
    --card: #ffffff;
    --brand-blue: #1a7fd0;
    --ink: #2b2b2b;
    --rule: #c9c9c9;
  }
  html, body {
    margin: 0;
    width: 1200px;
    height: 900px;
    overflow: hidden;
    background: var(--backdrop);
    font-family: "Lato", Arial, sans-serif;
  }
  .card {
    position: absolute;
    left: 180px;
    top: 210px;
    width: 840px;
    height: 480px;
    background: var(--card);
  }
  .brand {
    position: absolute;
    left: 80px;
    top: 222px;
    width: 330px;
  }
  .brand-name {
    display: flex;
    align-items: center;
    gap: 10px;
    font-size: 26px;
    font-weight: 400;
    letter-spacing: 0.5px;
    color: var(--brand-blue);
    text-transform: uppercase;
    white-space: nowrap;
  }
  .brand-dot {
    width: 32px;
    height: 32px;
    border-radius: 50%;
    background: var(--brand-blue);
    flex: none;
  }
  .brand-tagline {
    margin-top: 14px;
    font-size: 20px;
    color: var(--ink);
    letter-spacing: 0.2px;
    white-space: nowrap;
  }
  .divider {
    position: absolute;
    left: 440px;
    top: 110px;
    width: 1px;
    height: 270px;
    background: var(--rule);
  }
  .contact {
    position: absolute;
    left: 470px;
    top: 92px;
    color: var(--ink);
  }
  .person-name {
    margin: 0;
    font-size: 29px;
    font-weight: 900;
    color: var(--brand-blue);
    letter-spacing: 0.5px;
    text-transform: uppercase;
  }
  .person-title {
    margin: 2px 0 4px 12px;
    font-size: 17px;
  }
  .address {
    margin: 0 0 10px 24px;
    font-size: 18px;
    line-height: 1.3;
  }
  .lines {
    list-style: none;
    margin: 0 0 0 42px;
    padding: 0;
    font-size: 19px;
    line-height: 1.25;
  }
  .lines li {
    display: flex;
    align-items: center;
    gap: 8px;
  }
  .lines svg {
    width: 14px;
    height: 14px;
    fill: var(--brand-blue);
    flex: none;
  }
  .license {
    margin: 8px 0 0 56px;
    font-size: 20px;
  }
  .license-label { color: var(--brand-blue); }
</style>
</head>
<body>
  <main class="card">
    <div class="brand">
      <div class="brand-name"><span class="brand-dot"></span>Veltra Dunmore</div>
      <div class="brand-tagline">Architecture + Interior Design</div>
    </div>

    <div class="divider"></div>

    <section class="contact">
      <h1 class="person-name">Julian Harwick</h1>
      <div class="person-title">Partner / Director of Design</div>
      <div class="address">417 Marlowe West<br>Palm Beach 33401</div>
      <ul class="lines">
        <li><svg viewBox="0 0 16 16" aria-hidden="true"><path d="M1 4c0-2 2-3 7-3s7 1 7 3v2h-4V4H5v2H1zM4 7h8l2 7H2z"/></svg>561.555.0142</li>
        <li><svg viewBox="0 0 16 16" aria-hidden="true"><path d="M4 0h8a1 1 0 0 1 1 1v14a1 1 0 0 1-1 1H4a1 1 0 0 1-1-1V1a1 1 0 0 1 1-1zm1 2v10h6V2zm3 11a1 1 0 1 0 0 2 1 1 0 0 0 0-2z"/></svg>561.555.0187</li>
        <li><svg viewBox="0 0 16 16" aria-hidden="true"><path d="M4 0h8v5H4zM1 6h14v7h-3v3H4v-3H1zm5 5v3h4v-3z"/></svg>561.555.0163</li>
        <li><svg viewBox="0 0 16 16" aria-hidden="true"><path d="M0 3h16v1L8 9 0 4zm0 3 8 5 8-5v7H0z"/></svg>julian@veltradunmore.com</li>
        <li><svg viewBox="0 0 16 16" aria-hidden="true"><circle cx="8" cy="8" r="7.5"/></svg>www.veltradunmore.com</li>
      </ul>
      <div class="license"><span class="license-label">LIC</span> # AA26004817</div>
    </section>
  </main>
</body>
</html>
```